Wildlife photographer Website

The website is to be a "resume" of pictures and awards won by Nora. Pelham heavy to outdoor wildlife.
She will post articles and have ability to interact with fans.

I will add some of her pictures tonight,

Target Market(s)

Terrain Chronicle .....anyone looking to hire a wildlife photographer.

Industry/Entity Type

Professional Photography

Contact Information for Business Card

Nora Pelham
4817 Quiet Harbor Lane
Alder Falls NH 38512
518-264-8391
Nora@BrushNora.com

Coding

Coded - Design and coding required

Number of Pages Required

5+ page

Requirements
Must have
• New Logo
Nice to have
• Nature, and eye catching graphics

```html
<!DOCTYPE html>
<html lang="en">
<head>
<meta charset="utf-8">
<title>Wildlife Photography by Nora Pelham</title>
<link href="https://fonts.googleapis.com/css2?family=Teko:wght@500;600;700&family=Poppins:wght@400;500;600&display=swap" rel="stylesheet">
<style>
  :root {
    --stage: #eeeeee;
    --ink: #000000;
    --paper: #ffffff;
    --muted: #c9c9c9;
    --soft: #9a9a9a;
    --veil: rgba(190, 180, 165, 0.35);
    --head: "Teko", "Arial Narrow", sans-serif;
    --body: "Poppins", Arial, sans-serif;
  }
  * { margin: 0; padding: 0; box-sizing: border-box; }
  html, body { width: 1200px; height: 3333px; overflow: hidden; background: var(--stage); }
  .page { position: absolute; left: 153px; top: 0; width: 894px; height: 3333px; background: var(--ink); color: var(--paper); font-family: var(--body); overflow: hidden; }
  .abs { position: absolute; }
  .photo { position: absolute; }

  /* hero */
  .hero { position: absolute; left: 0; top: 0; width: 894px; height: 452px;
    background:
      linear-gradient(to bottom, rgba(0,0,0,0) 55%, #000 100%),
      radial-gradient(ellipse 260px 180px at 640px 60px, #ffd24a 0%, rgba(244,178,28,.7) 35%, rgba(0,0,0,0) 100%),
      radial-gradient(ellipse 380px 220px at 500px 320px, #c2561a 0%, rgba(120,40,10,.6) 60%, rgba(0,0,0,0) 100%),
      linear-gradient(100deg, #5a1608 0%, #9c3510 40%, #d77a19 70%, #6a1d09 100%); }
  .logo { left: 79px; top: 26px; font-family: var(--head); font-weight: 600; font-size: 15px; letter-spacing: 1px; }
  .menu { left: 798px; top: 28px; }
  .hero-by { left: 212px; top: 210px; font-family: var(--head); font-weight: 600; font-size: 14px; letter-spacing: 5px; line-height: 1; }
  .hero-title { left: 206px; top: 222px; font-family: var(--head); font-weight: 700; font-size: 118px; letter-spacing: 8px; line-height: 1; }
  .hero-sub { left: 548px; top: 318px; font-family: var(--head); font-weight: 600; font-size: 14px; letter-spacing: 6px; line-height: 1; }

  /* shared */
  .h-section { font-family: var(--head); font-weight: 600; line-height: 1; }
  .copy { font-size: 9.5px; line-height: 19px; color: var(--paper); }
  .btn { position: absolute; background: var(--paper); color: var(--ink); font-size: 10px; display: flex; align-items: center; justify-content: center; border-radius: 2px; }
  .kicker { font-family: var(--head); font-weight: 600; font-style: italic; font-size: 10px; letter-spacing: .5px; }
  .rule { height: 1px; width: 66px; background: var(--paper); }

  /* about */
  .about-title { left: 434px; top: 540px; font-size: 30px; }
  .about-copy { left: 434px; top: 584px; width: 330px; }
  .btn-about { left: 434px; top: 786px; width: 103px; height: 30px; }

  /* features */
  .feature-text { position: absolute; width: 350px; }
  .feature-text .kicker { display: block; margin-bottom: 8px; }
  .feature-text .h-section { font-size: 26px; }
  .feature-text .rule { margin: 2px 0 10px; }
  .feature-text .copy { font-size: 7.8px; line-height: 13.5px; }

  /* exclusive */
  .centered { position: absolute; left: 0; width: 894px; text-align: center; }
  .excl-title { top: 1540px; font-size: 32px; }
  .excl-sub { top: 1586px; font-size: 10px; line-height: 17px; }
  .card { position: absolute; width: 229px; text-align: center; }
  .card .photo { position: relative; width: 229px; height: 206px; }
  .card-title { margin-top: 22px; font-family: var(--head); font-weight: 600; font-size: 11px; letter-spacing: .3px; }
  .card-copy { margin: 6px auto 0; width: 200px; font-size: 7.6px; line-height: 12.5px; color: var(--muted); }
  .card-link { margin-top: 10px; font-size: 9.5px; }

  /* conservation band */
  .band { left: 0; top: 2060px; width: 894px; height: 520px;
    background:
      linear-gradient(to bottom, #000 0%, rgba(0,0,0,0) 12%, rgba(0,0,0,0) 85%, #000 100%),
      radial-gradient(ellipse 300px 200px at 450px 250px, #a08a70 0%, rgba(0,0,0,0) 100%),
      linear-gradient(135deg, #6e5c48 0%, #8f7a62 45%, #5d4d3c 100%); }
  .veil { left: 166px; top: 2120px; width: 564px; height: 387px; background: var(--veil); }
  .veil-frame { left: 187px; top: 2141px; width: 521px; height: 346px; border: 1px solid rgba(30,25,20,.7); }
  .band-title { left: 187px; top: 2262px; width: 521px; text-align: center; font-family: var(--head); font-weight: 600; font-size: 31px; line-height: 31px; color: #111; }
  .btn-dark { left: 378px; top: 2364px; width: 139px; height: 34px; background: var(--ink); color: var(--paper); font-size: 12px; }

  /* articles */
  .art-title { top: 2616px; font-size: 38px; }
  .art-sub { top: 2662px; font-size: 10px; line-height: 17px; }
  .article .card-title { margin-top: 16px; }
  .art-copy { margin-top: 4px; font-size: 11px; line-height: 17px; color: var(--muted); }
  .art-rule { width: 36px; height: 1px; background: var(--soft); margin: 11px auto 8px; }
  .art-date { font-size: 7.5px; font-style: italic; color: var(--muted); }

  /* footer */
  .foot-title { font-family: var(--head); font-weight: 600; font-size: 15px; letter-spacing: .3px; }
  .foot-head { font-family: var(--body); font-weight: 400; font-size: 12px; }
  .foot-col { position: absolute; top: 3142px; }
  .foot-copy { margin-top: 16px; width: 165px; font-size: 8px; line-height: 13px; color: var(--muted); }
  .foot-list { list-style: none; margin-top: 12px; }
  .foot-list li { font-size: 8.5px; line-height: 19px; color: var(--muted); display: flex; align-items: center; }
  .foot-list li::before { content: ""; width: 4px; height: 4px; border-radius: 50%; background: var(--paper); margin-right: 18px; }
  .social { display: flex; gap: 16px; margin-top: 14px; margin-left: 4px; }
  .social span { width: 11px; height: 11px; border-radius: 50%; border: 1.5px solid var(--paper); }
  .contact-row { display: flex; gap: 14px; font-size: 8.5px; line-height: 14px; color: var(--muted); margin-top: 12px; }
  .contact-row svg { flex: none; margin-top: 2px; }
  .foot-divider { left: 55px; top: 3308px; width: 788px; height: 1px; background: #333; }
  .copyright { top: 3316px; font-size: 7.5px; color: var(--muted); }
</style>
</head>
<body>
<main class="page">

  <header class="hero" role="img" aria-label="Tiger resting on a fallen log at sunset, warm orange and golden light"></header>
  <div class="abs logo">LOGO HERE</div>
  <svg class="abs menu" width="14" height="12" viewBox="0 0 14 12" aria-label="Menu">
    <rect x="0" y="1" width="14" height="1.6" fill="#fff"/>
    <rect x="0" y="5.2" width="14" height="1.6" fill="#fff"/>
    <rect x="0" y="9.4" width="14" height="1.6" fill="#fff"/>
  </svg>
  <div class="abs hero-by">BY NORA.PELHAM</div>
  <h1 class="abs hero-title">WILDLIFE</h1>
  <div class="abs hero-sub">PHOTOGRAPHY</div>

  <section>
    <div class="photo" style="left:110px;top:517px;width:256px;height:322px;background:linear-gradient(180deg,#3d5a3a 0%,#587352 40%,#7a8f86 70%,#5b6e6a 100%)" role="img" aria-label="Portrait of the photographer standing by a forest river holding a phone"></div>
    <h2 class="abs h-section about-title">BY NORA. PELHAM</h2>
    <p class="abs copy about-copy">Lorem ipsum dolor sit amet, consectetur adipiscing elit. Diam erat amet eget velit cursus venenatis in. Sit sodales pulvinar elementum erat enim sollicitudin elit pulvinar a. Porttitor interdum elit eget suspendisse imperdiet gravida sit a. Id ut venenatis, tincidunt suscipit. Parturient volutpat faucibus semper et lobortis neque. Eu, quam nisi, ullamcorper varius. Quis nunc enim in aliquam. Purus risus enim tincidunt id pharetra enim diam vitae pulvinar. Gravida arcu ultrices ipsum risus, at consequat.</p>
    <div class="btn btn-about">Learn More</div>
  </section>

  <section>
    <div class="feature-text" style="left:36px;top:924px">
      <span class="kicker">DUCK FROM AMAZON JUNGLE</span>
      <h3 class="h-section">LOREM IPSUM</h3>
      <div class="rule"></div>
      <p class="copy">Lorem ipsum dolor sit amet, consectetur adipiscing elit. Pharetra maecenas ipsum fringilla orci nec risus sed egestas pellentesque. Tristique faucibus proin sed pharetra, auctor neque, arcu, tincidunt. Aliquet tellus mauris, at aliquam maecenas sit duis vel elit. Aliquam maecenas ut tortor elementum, facilisis sit. Dolor sapien arcu ligula turpis iaculis habitasse mauris. Natoque consequat suscipit cursus eu elementum integer. Pretium convallis scelerisque viverra malesuada imperdiet.</p>
    </div>
    <div class="btn" style="left:32px;top:1110px;width:103px;height:27px">View Gallery</div>
    <div class="photo" style="left:440px;top:890px;width:454px;height:293px;background:linear-gradient(160deg,#7fa6bf 0%,#3d6f8f 45%,#214d6a 100%)" role="img" aria-label="Long-tailed duck swimming on blue water"></div>

    <div class="photo" style="left:0;top:1183px;width:440px;height:293px;background:linear-gradient(135deg,#4a3a22 0%,#6d5430 40%,#a86a2e 60%,#3f4a2a 100%)" role="img" aria-label="Red fox sitting among fallen branches and autumn leaves"></div>
    <div class="feature-text" style="left:472px;top:1224px">
      <span class="kicker">FOX FROM AMAZON JUNGLE</span>
      <h3 class="h-section">LOREM IPSUM</h3>
      <div class="rule"></div>
      <p class="copy">Lorem ipsum dolor sit amet, consectetur adipiscing elit. Pharetra maecenas ipsum fringilla orci nec risus sed egestas pellentesque. Tristique faucibus proin sed pharetra, auctor neque, arcu, tincidunt. Aliquet tellus mauris, at aliquam maecenas sit duis vel elit. Aliquam maecenas ut tortor elementum, facilisis sit. Dolor sapien arcu ligula turpis iaculis habitasse mauris. Natoque consequat suscipit cursus eu elementum integer. Pretium convallis scelerisque viverra malesuada imperdiet.</p>
    </div>
    <div class="btn" style="left:469px;top:1410px;width:103px;height:27px">View Gallery</div>
  </section>

  <section>
    <h2 class="centered h-section excl-title">WILD'S EXCLUSIVE | JUST FOR YOU!</h2>
    <p class="centered excl-sub">All free content to see, read and download for personal use<br>only. Spread the love for wildlife!</p>

    <article class="card" style="left:56px;top:1668px">
      <div class="photo" style="background:linear-gradient(180deg,#3b5f8f 0%,#7c9cc4 55%,#dfe7f1 100%)" role="img" aria-label="Hare leaping across snow by a river"></div>
      <h4 class="card-title">WILD TIGER MOTHER WITH TWO CUBS</h4>
      <p class="card-copy">Browse Through Free Content On How To Start Photography, Choosing The Right Camera And Lens, Wildlife Photography Tips And Techniques, Field Guides And Nuances Of Wildlife Photography.</p>
      <div class="card-link">Browse&gt;&gt;&gt;</div>
    </article>
    <article class="card" style="left:335px;top:1668px">
      <div class="photo" style="background:linear-gradient(180deg,#b6b58c 0%,#8a8458 50%,#6a6242 100%)" role="img" aria-label="Duck flapping its wings on rippled water"></div>
      <h4 class="card-title">WILD TIGER MOTHER WITH TWO CUBS</h4>
      <p class="card-copy">Browse Through Free Content On How To Start Photography, Choosing The Right Camera And Lens, Wildlife Photography Tips And Techniques, Field Guides And Nuances Of Wildlife Photography.</p>
      <div class="card-link">Browse&gt;&gt;&gt;</div>
    </article>
    <article class="card" style="left:614px;top:1668px">
      <div class="photo" style="background:linear-gradient(180deg,#6f8fb3 0%,#a7b3b8 40%,#c9a36a 70%,#b98c52 100%)" role="img" aria-label="Sandpiper standing on a sandy beach"></div>
      <h4 class="card-title">WILD TIGER MOTHER WITH TWO CUBS</h4>
      <p class="card-copy">Browse Through Free Content On How To Start Photography, Choosing The Right Camera And Lens, Wildlife Photography Tips And Techniques, Field Guides And Nuances Of Wildlife Photography.</p>
      <div class="card-link">Browse&gt;&gt;&gt;</div>
    </article>
  </section>

  <section>
    <div class="abs band" role="img" aria-label="Hummingbird in flight over sandy earth, muted brown tones"></div>
    <div class="abs veil"></div>
    <div class="abs veil-frame"></div>
    <h2 class="abs band-title">WE CONTRIBUTE TO WILDLIFE<br>CONSERVATION THROUGH WILDLIFE<br>PHOTOGRAPHY</h2>
    <div class="btn btn-dark">Contact Us</div>
  </section>

  <section>
    <h2 class="centered h-section art-title">WILD ARTICLE</h2>
    <p class="centered art-sub">Wild Stories from american Jungle, Wildlife Travelogue, Nuances of Wildlife Photography<br>and much more...</p>

    <article class="card article" style="left:55px;top:2732px">
      <div class="photo" style="background:linear-gradient(160deg,#c9903f 0%,#8a5a25 50%,#4a2f15 100%)" role="img" aria-label="Otter swimming in golden water"></div>
      <h4 class="card-title">WILDLIFE PHOTOGRAPHY</h4>
      <p class="art-copy">Lorem Ipsum Dolor Sit Amet,<br>Consectetur Adipiscing Elit.</p>
      <div class="art-rule"></div>
      <div class="art-date">Jan 5, 2021</div>
    </article>
    <article class="card article" style="left:328px;top:2732px">
      <div class="photo" style="background:linear-gradient(180deg,#d8d2c4 0%,#c8bfae 60%,#9c8f74 85%,#3f5d8a 100%)" role="img" aria-label="Flock of small birds flying over reeds"></div>
      <h4 class="card-title">WILDLIFE PHOTOGRAPHY</h4>
      <p class="art-copy">Lorem Ipsum Dolor Sit Amet,<br>Consectetur Adipiscing Elit.</p>
      <div class="art-rule"></div>
      <div class="art-date">Jan 5, 2021</div>
    </article>
    <article class="card article" style="left:615px;top:2732px">
      <div class="photo" style="background:linear-gradient(180deg,#2f5e9a 0%,#1f477c 55%,#173a66 100%)" role="img" aria-label="Harlequin ducks floating on deep blue water"></div>
      <h4 class="card-title">WILDLIFE PHOTOGRAPHY</h4>
      <p class="art-copy">Lorem Ipsum Dolor Sit Amet,<br>Consectetur Adipiscing Elit.</p>
      <div class="art-rule"></div>
      <div class="art-date">Jan 5, 2021</div>
    </article>
  </section>

  <footer>
    <div class="foot-col" style="left:65px">
      <h5 class="foot-title">WILD PHOTOGRAPY</h5>
      <p class="foot-copy">lorem ipsum dolor sit amet, consectetur adipiscing elit. viverra et pellentesque leo imperdiet quis. a diam ut natoque amet sodales. id amet, viverra vitae et enim.</p>
      <div class="social" aria-label="Social links"><span></span><span></span><span></span><span></span></div>
    </div>
    <div class="foot-col" style="left:298px">
      <h5 class="foot-head">ABOUT US</h5>
      <ul class="foot-list">
        <li>Our Article</li><li>Photo Feeds</li><li>Our Mission</li><li>Our Story</li>
      </ul>
    </div>
    <div class="foot-col" style="left:479px">
      <h5 class="foot-head">QUICK LINKS</h5>
      <ul class="foot-list" style="margin-top:8px">
        <li>Our Gallery</li><li>Wild Life</li><li>Wild Life Video</li><li>Wild Life Photos</li><li>FAQ</li>
      </ul>
    </div>
    <div class="foot-col" style="left:671px">
      <h5 class="foot-head">CONTACT US</h5>
      <div class="contact-row">
        <svg width="10" height="10" viewBox="0 0 24 24"><path d="M6.6 10.8a15 15 0 0 0 6.6 6.6l2.2-2.2c.3-.3.7-.4 1-.2 1.1.4 2.3.6 3.6.6.6 0 1 .4 1 1V20c0 .6-.4 1-1 1A17 17 0 0 1 3 4c0-.6.4-1 1-1h3.5c.6 0 1 .4 1 1 0 1.3.2 2.5.6 3.6.1.3 0 .7-.2 1z" fill="#fff"/></svg>
        <span>518-264-8391</span>
      </div>
      <div class="contact-row">
        <svg width="10" height="10" viewBox="0 0 24 24"><rect x="2" y="5" width="20" height="14" fill="none" stroke="#aaa" stroke-width="2"/><path d="M2 5l10 8 10-8" fill="none" stroke="#aaa" stroke-width="2"/></svg>
        <span>Nora@BrushNora.com</span>
      </div>
      <div class="contact-row">
        <svg width="10" height="12" viewBox="0 0 24 28"><path d="M12 2a8 8 0 0 0-8 8c0 6 8 16 8 16s8-10 8-16a8 8 0 0 0-8-8z" fill="none" stroke="#ccc" stroke-width="2.2"/><circle cx="12" cy="10" r="3" fill="none" stroke="#ccc" stroke-width="2.2"/></svg>
        <span>Nora Pelham 4817 Quiet<br>Harbor Lane Alder Falls NH<br>38512</span>
      </div>
    </div>
    <div class="abs foot-divider"></div>
    <p class="centered copyright">Copyright 2021 WildNora All Rights Reserved</p>
  </footer>

</main>
</body>
</html>
```